Bref créative
The Lanternwrights
We get IT done right!
Professional
Rosalind Kettering
Partner
48 Thornapple Lane
Marrowdale, PA 19522
rosalind.k.kettering@thelanternwrights.net
www.thelanternwrights.net
logo will be attached
second set of business cards needed
Dean Oltveld
dean.oltveld@thelanternwrights.net
Counsel You Can Count On
Updated logo in CMYK format

```html
<!DOCTYPE html>
<html lang="en">
<head>
<meta charset="utf-8">
<title>The Lanternwrights – Stationery Set</title>
<link href="https://fonts.googleapis.com/css2?family=Arimo:wght@400;700&display=swap" rel="stylesheet">
<style>
  :root {
    --page-bg: #ffffff;
    --frame: #d9d9d9;
    --paper: #ffffff;
    --ink: #1f1f1f;
    --ink-soft: #555555;
    --brand-red: #d8232a;
    --brand-orange: #f08a24;
    --mark-faint: rgba(240, 138, 36, 0.16);
    --shadow: rgba(0, 0, 0, 0.22);
  }
  * { box-sizing: border-box; margin: 0; padding: 0; }
  html, body {
    width: 1200px; height: 681px; overflow: hidden;
    background: var(--page-bg);
    font-family: "Arimo", Arial, sans-serif;
    color: var(--ink);
  }
  .stage { position: relative; width: 1200px; height: 681px; }
  .stage-frame {
    position: absolute; left: 12px; top: 12px; right: 12px; bottom: 12px;
    border: 1px solid var(--frame);
  }
  .sheet {
    position: absolute; background: var(--paper);
    box-shadow: 1px 2px 5px var(--shadow);
    overflow: hidden;
  }

  /* brand lockup */
  .brand-mark {
    display: block; border-radius: 50%;
    background: radial-gradient(circle at 35% 35%, var(--brand-orange), var(--brand-red));
  }
  .brand-mark-faint {
    position: absolute; display: block; border-radius: 50%;
    background: var(--mark-faint);
  }
  .brand-name {
    font-weight: 700; text-transform: uppercase; color: var(--ink);
    white-space: nowrap; letter-spacing: 0.02em;
  }
  .brand-row { display: flex; align-items: center; }
  .brand-rule { flex: 1; height: 1.5px; background: var(--brand-red); margin-left: 6px; }

  /* envelope front */
  .envelope-front { left: 29px; top: 96px; width: 528px; height: 204px; }
  .envelope-front .brand-mark { position: absolute; left: 24px; top: 14px; width: 40px; height: 40px; }
  .envelope-front .brand-row { position: absolute; left: 14px; right: 0; top: 60px; }
  .envelope-front .brand-name { font-size: 14px; }
  .envelope-front .return-address { position: absolute; left: 14px; top: 84px; font-size: 8px; font-weight: 700; }

  /* envelope back */
  .envelope-back { left: 43px; top: 396px; width: 514px; height: 204px; }
  .envelope-back .flap { position: absolute; inset: 0; width: 100%; height: 100%; }
  .envelope-back .brand-mark { position: absolute; left: 236px; top: 64px; width: 42px; height: 42px; }

  /* letterhead */
  .letterhead { left: 607px; top: 48px; width: 360px; height: 564px; }
  .letterhead .brand-mark { position: absolute; left: 26px; top: 18px; width: 44px; height: 44px; }
  .letterhead .brand-row { position: absolute; left: 14px; right: 0; top: 70px; }
  .letterhead .brand-name { font-size: 14px; }
  .letterhead .contact-block { position: absolute; left: 14px; top: 96px; font-size: 8px; font-weight: 700; line-height: 1.35; font-style: normal; }
  .letterhead .brand-mark-faint { right: -30px; bottom: 20px; width: 190px; height: 190px; }

  /* business cards */
  .card { width: 132px; height: 90px; }
  .card-front { left: 960px; top: 186px; }
  .card-front .brand-mark { position: absolute; left: 9px; top: 6px; width: 18px; height: 18px; }
  .card-front .brand-name { position: absolute; left: 5px; top: 28px; font-size: 6.5px; }
  .card-front .person-name { position: absolute; left: 5px; top: 40px; font-size: 6px; font-weight: 700; color: var(--brand-red); }
  .card-front .person-title { position: absolute; left: 5px; top: 48px; font-size: 4.5px; font-weight: 700; }
  .card-front .person-contact { position: absolute; left: 5px; top: 58px; font-size: 3.6px; line-height: 1.35; }
  .card-front .brand-mark-faint { right: -8px; top: 34px; width: 40px; height: 40px; }

  .card-back { left: 960px; top: 365px; }
  .card-back .brand-mark { position: absolute; left: 56px; top: 18px; width: 20px; height: 20px; }
  .card-back .brand-name { position: absolute; left: 0; right: 0; top: 42px; text-align: center; font-size: 6.5px; }
  .card-back .card-slogan { position: absolute; left: 0; right: 0; top: 56px; text-align: center; font-size: 5px; font-weight: 700; }
</style>
</head>
<body>
<main class="stage">
  <div class="stage-frame"></div>

  <section class="sheet envelope-front" aria-label="Envelope front">
    <span class="brand-mark"></span>
    <div class="brand-row"><span class="brand-name">The Lanternwrights</span><span class="brand-rule"></span></div>
    <p class="return-address">48 Thornapple Lane, Marrowdale, PA 19522</p>
  </section>

  <section class="sheet envelope-back" aria-label="Envelope back">
    <svg class="flap" viewBox="0 0 514 204" preserveAspectRatio="none" aria-hidden="true">
      <path d="M2 2 Q6 30 60 32 L454 32 Q508 30 512 2" fill="none" stroke="#555" stroke-width="1"/>
    </svg>
    <span class="brand-mark"></span>
  </section>

  <section class="sheet letterhead" aria-label="Letterhead">
    <span class="brand-mark"></span>
    <div class="brand-row"><span class="brand-name">The Lanternwrights</span><span class="brand-rule"></span></div>
    <address class="contact-block">
      48 Thornapple Lane<br>
      Marrowdale, PA 19522<br>
      rosalind.k.kettering@thelanternwrights.net<br>
      www.thelanternwrights.net
    </address>
    <span class="brand-mark-faint"></span>
  </section>

  <section class="sheet card card-front" aria-label="Business card front">
    <span class="brand-mark-faint"></span>
    <span class="brand-mark"></span>
    <span class="brand-name">The Lanternwrights</span>
    <p class="person-name">Rosalind Kettering</p>
    <p class="person-title">Partner</p>
    <p class="person-contact">
      48 Thornapple Lane<br>
      Marrowdale, PA 19522<br>
      tel 610.555.0142<br>
      rosalind.k.kettering@thelanternwrights.net<br>
      www.thelanternwrights.net
    </p>
  </section>

  <section class="sheet card card-back" aria-label="Business card back">
    <span class="brand-mark"></span>
    <span class="brand-name">The Lanternwrights</span>
    <p class="card-slogan">Counsel You Can Count On</p>
  </section>
</main>
</body>
</html>
```